Letterhead in Word Format

We are a small law firm in the Midwest. Our clientele is generally small business owners and companies.

We recently had a complete re-brand with a new logo, new letterhead, business cards, etc. However, the major issue now is that we cannot use the letterhead without physically ordering letterhead. Thus, invoices, and other items cannot be custom drafted.

We require custom letterhead in MICROSOFT WORD format. Our logo will be provided to you. And we will also provide a copy of the letterhead that was prepared.

We would like to see designs that are black and white, sophisticated, elegant, and generally professional. We prefer a traditional design with just a touch of contemporary.

Please do not submit any designs that are not Microsoft Word compatible.

EDIT: Please view the attached letterhead. The design must include the logo, name, address, fax, phone, email, and name of attorney.
Updates

Thank you all for submitting designs. I just wanted to quickly provide some feedback. I saw a few designs that had the logo at the bottom. Because there will be text with margins at 1" all around, it's not practical have the logo at the bottom. Also, designs with blocks of gray or black would cause our printer to bleed black onto the letterhead, so that is not practical as well.

If you have any comments, please feel free to leave me a message. Thank you.

Target Market(s)

Small business owners, companies, real estate investors and developers.

Industry/Entity Type

Small Business

Font styles to use
Script

Requirements
Must have
• Microsoft Word Format

```html
<!DOCTYPE html>
<html lang="en">
<head>
<meta charset="utf-8">
<title>The Whitford Law Firm – Letterhead</title>
<link href="https://fonts.googleapis.com/css2?family=Open+Sans:wght@400;600;700&family=Libre+Baskerville&display=swap" rel="stylesheet">
<style>
  :root {
    --backdrop: #e4e4e2;
    --paper: #ffffff;
    --ink: #1a1a1a;
    --ink-soft: #3a3a3a;
    --muted: #8a8a8a;
    --rule: #9a9a9a;
    --watermark: #ececec;
  }
  * { margin: 0; padding: 0; box-sizing: border-box; }
  html, body { width: 1200px; height: 1091px; overflow: hidden; }
  body {
    background: var(--backdrop);
    font-family: "Open Sans", Arial, sans-serif;
    color: var(--ink);
    position: relative;
  }
  .letterhead {
    position: absolute;
    left: 198px; top: 24px;
    width: 804px; height: 1040px;
    background: var(--paper);
    box-shadow: 0 2px 10px rgba(0,0,0,0.12);
  }
  .attorney { position: absolute; left: 72px; top: 62px; }
  .attorney-name {
    font-weight: 700; font-size: 17px; letter-spacing: 2px; text-transform: uppercase;
  }
  .attorney-title { font-size: 11px; color: var(--ink-soft); margin-top: 1px; }

  .firm-name {
    position: absolute; right: 72px; top: 66px;
    display: flex; align-items: center; gap: 12px;
    font-family: "Libre Baskerville", Georgia, serif;
    font-size: 17px; letter-spacing: 1px; color: var(--ink-soft);
  }
  .firm-name .mark { width: 38px; height: 38px; border-radius: 50%; border: 1px solid var(--rule); }

  .contact {
    position: absolute; right: 72px; top: 176px;
    text-align: right; font-size: 13px; font-weight: 600; line-height: 1.45;
    font-style: normal;
  }

  .watermark {
    position: absolute; left: 210px; top: 430px; width: 380px; height: 230px;
    border-radius: 50%;
    background: radial-gradient(ellipse at center, #e2e2e2 0%, var(--watermark) 55%, rgba(255,255,255,0) 75%);
  }

  .body-copy { position: absolute; left: 72px; top: 268px; width: 660px; }
  .body-heading {
    font-size: 9px; letter-spacing: 0.5px; text-transform: uppercase;
    color: var(--muted); margin-bottom: 14px;
  }
  .body-copy p {
    font-size: 13px; line-height: 1.62; color: var(--ink-soft); margin-bottom: 24px;
  }

  .signature {
    position: absolute; left: 72px; top: 820px; width: 150px; height: 50px;
    background: linear-gradient(90deg, #f2f2f2, #e8e8e8 50%, #f4f4f4);
    border-radius: 25px;
  }

  .footer {
    position: absolute; left: 72px; right: 72px; bottom: 52px;
    border-top: 1px solid var(--rule); padding-top: 8px;
    font-size: 12px; color: var(--ink-soft);
  }
  .footer .sep { margin: 0 8px; color: var(--muted); }
</style>
</head>
<body>
  <main class="letterhead">
    <header class="attorney">
      <div class="attorney-name">Daniel R. Whitford</div>
      <div class="attorney-title">Principal Attorney</div>
    </header>

    <div class="firm-name">
      <span class="mark"></span>
      <span>THE WHITFORD LAW FIRM</span>
    </div>

    <address class="contact">
      <div>Fax: (555) 014-2279</div>
      <div>Phone: (555) 014-2280</div>
      <div>Email: info@whitfordlawfirm.com</div>
    </address>

    <div class="watermark" role="img" aria-label="Faint decorative quill emblem behind the letter text"></div>

    <section class="body-copy">
      <div class="body-heading">Lorem Ipsum Dummy Text</div>
      <p>Lorem Ipsum is simply dummy text of the printing and typesetting industry. Lorem Ipsum has been the industry's standard dummy text ever since the 1500s, when an unknown printer took a galley of type and scrambled it to make a type specimen book. It has survived not only five centuries, but also the leap into electronic typesetting, remaining essentially unchanged. It was popularised in the 1960s with the release of Lettrafix sheets containing Lorem Ipsum passages, and more recently with desktop publishing software like Pagewright Studio including versions of Lorem Ipsum.</p>
      <p>Lorem Ipsum is simply dummy text of the printing and typesetting industry. Lorem Ipsum has been the industry's standard dummy text ever since the 1500s, when an unknown printer took a galley of type and scrambled it to make a type specimen book. It has survived not only five centuries, but also the leap into electronic typesetting, remaining essentially unchanged. It was popularised in the 1960s with the release of Lettrafix sheets containing Lorem Ipsum passages, and more recently with desktop publishing software like Pagewright Studio including versions of Lorem Ipsum.</p>
    </section>

    <div class="signature" role="img" aria-label="Handwritten attorney signature"></div>

    <footer class="footer">
      whitfordlawfirm.com<span class="sep">|</span>2150 W. Harlan Ave Brookfield, Illinois 60513
    </footer>
  </main>
</body>
</html>
```